Apartment Investor Business Card Design

Need a new business card designed for my multifamily investment company

Industry/Entity Type

Real Estate

Contact Information for Business Card

Marlow Pickett - President & CEO
Brightfield Capital, LLC
4870 North 52nd Avenue, Ste 150
Omaha, NE 68231
(402) 555-0193
Marlow@brightfieldcapitalmidwest.example
Www.BrightfieldCapitalMidwest.example

Colors
3176b5

```html
<!DOCTYPE html>
<html lang="en">
<head>
<meta charset="utf-8">
<title>Brightfield Capital – Business Card</title>
<link href="https://fonts.googleapis.com/css2?family=Bebas+Neue&family=Cinzel&family=PT+Sans:wght@400;700&display=swap" rel="stylesheet">
<style>
  :root {
    --backdrop: #5b88c7;
    --card: #1b1b1b;
    --ink: #ffffff;
    --accent: #3176b5;
    --accent-soft: #5a8fd0;
    --muted: #e8e8e8;
  }
  * { margin: 0; padding: 0; box-sizing: border-box; }
  html, body {
    width: 1200px; height: 1200px; overflow: hidden;
    background: var(--backdrop);
  }
  .card {
    position: absolute;
    left: 223px;
    width: 815px; height: 466px;
    background: var(--card);
    color: var(--ink);
    font-family: "PT Sans", sans-serif;
  }
  .card--front { top: 76px; }
  .card--back { top: 658px; }

  .wordmark {
    position: absolute;
    font-family: "Cinzel", serif;
    font-weight: 400;
    color: var(--ink);
    white-space: nowrap;
    letter-spacing: 0.5px;
    line-height: 1;
  }
  .card--front .wordmark {
    right: 49px; top: 170px;
    font-size: 31px;
  }
  .card--back .wordmark {
    left: 0; width: 858px; text-align: center;
    top: 278px;
    font-size: 44px;
  }

  .person__name {
    position: absolute; left: 46px; top: 296px;
    font-family: "Bebas Neue", sans-serif;
    font-size: 36px; line-height: 1; letter-spacing: 0.3px;
  }
  .person__title {
    position: absolute; left: 46px; top: 332px;
    font-size: 16px; line-height: 20px; color: var(--accent-soft);
  }
  .rule {
    position: absolute; left: 181px; top: 341px;
    width: 583px; height: 2px; background: var(--ink);
  }
  .contact {
    position: absolute; left: 46px; top: 360px;
    list-style: none;
  }
  .contact li {
    display: flex; align-items: center;
    height: 23px; font-size: 16px; color: var(--muted);
  }
  .contact svg { width: 14px; height: 14px; margin-right: 14px; flex: none; }
  .address {
    position: absolute; right: 51px; top: 383px;
    text-align: right; font-size: 16px; line-height: 23px; color: var(--muted);
  }
  .back-url {
    position: absolute; right: 29px; top: 416px;
    font-size: 12.5px; font-weight: 700; color: var(--ink);
  }
  .back-url span { color: var(--accent-soft); }
</style>
</head>
<body>

<section class="card card--front">
  <div class="wordmark">BRIGHTFIELD CAPITAL</div>

  <h1 class="person__name">Marlow Pickett</h1>
  <p class="person__title">President &amp; CEO</p>
  <div class="rule"></div>

  <ul class="contact">
    <li>
      <svg viewBox="0 0 24 24" aria-hidden="true"><path fill="#3176b5" d="M6.6 10.8a15.1 15.1 0 0 0 6.6 6.6l2.2-2.2c.3-.3.7-.4 1-.2 1.1.4 2.3.6 3.6.6.6 0 1 .4 1 1V20c0 .6-.4 1-1 1A17 17 0 0 1 3 4c0-.6.4-1 1-1h3.5c.6 0 1 .4 1 1 0 1.3.2 2.5.6 3.6.1.3 0 .7-.2 1z"/></svg>
      +(402) 555-0193
    </li>
    <li>
      <svg viewBox="0 0 24 24" aria-hidden="true"><rect x="2" y="5" width="20" height="14" fill="#3176b5"/><path d="M2 5l10 8 10-8" fill="none" stroke="#1b1b1b" stroke-width="1.6"/></svg>
      marlow@brightfieldcapitalmidwest.example
    </li>
    <li>
      <svg viewBox="0 0 24 24" aria-hidden="true"><g fill="none" stroke="#3176b5" stroke-width="1.6"><circle cx="12" cy="12" r="9"/><ellipse cx="12" cy="12" rx="4" ry="9"/><path d="M3 12h18M5 7h14M5 17h14"/></g></svg>
      www.BrightfieldCapitalMidwest.example
    </li>
  </ul>

  <address class="address" style="font-style:normal">
    Brightfield Capital, LLC 4870 North<br>
    52nd Avenue, Ste 150 Omaha, NE 68231
  </address>
</section>

<section class="card card--back">
  <div class="wordmark">BRIGHTFIELD CAPITAL</div>
  <p class="back-url">www.<span>BrightfieldCapitalMidwest</span>.example</p>
</section>

</body>
</html>
```